Construction Website Design for Wordpress

Update:
I like this theme as a starting point. It seems like a very good start. Fonts, colors, motion, etc. https://consultancy.qrvistaweb.com/
***************************************************************************************

I want a new website design that can be implemented in wordpress. Here is my existing site: www.halvornquantax.com
Attached is a document with the copy, requirements, sample images, etc. Let me know what questions you have.

Here is a sample of the info, but review the attached document for everything:

Website layout:
Title Bar
• Home
• Expertise
• Takeoffs
• Divisions Serviced (redesign from orig page: (http://www.halvornquantax.com/scope-list/)
• Member Login
Requirements
• Home page has a slider with 3 dimmed commercial construction images and copy overlay
• Request for Proposal Form should be over the slider and the same look and location on every page.
• “Request For Proposal” – No Obligation
o Company Name
o Contact Name
o Contact Phone
o Contact Email
• Use the copy below for the pages
• Split the Client Testimonials among the pages

Target Market(s)

B2B - Construction Companies

Industry/Entity Type

Construction

Number of Pages Required

4 page

Font styles to use
Serif

Colors
0255a3
3276b5
85abd2
d0dfed

Requirements
Must have
• Construction images in slider
• Request for proposal form
• testimonials

```html
<!DOCTYPE html>
<html lang="en">
<head>
<meta charset="utf-8">
<title>Halvorn Quantax – Construction Takeoff Experts</title>
<link href="https://fonts.googleapis.com/css2?family=Poppins:wght@300;400;500;600&family=Raleway:wght@300;400;600;700&display=swap" rel="stylesheet">
<style>
:root{
  --navy:#0b2f5e;
  --brand:#0255a3;
  --mid:#3276b5;
  --soft:#85abd2;
  --pale:#d0dfed;
  --deep:#1f4b8e;
  --cyan:#3fc1f0;
  --ink:#333a45;
  --grey:#8a8f98;
  --white:#ffffff;
}
*{box-sizing:border-box;margin:0;padding:0}
html,body{width:1200px;height:2828px;overflow:hidden}
body{position:relative;font-family:"Poppins",sans-serif;color:var(--ink);background:var(--white)}
.abs{position:absolute}

/* top bar */
.topbar{left:0;top:0;width:1200px;height:34px;background:var(--navy);color:#c9d6e8;font-size:10px}
.topbar .welcome{left:142px;top:10px}
.topbar .links{right:150px;top:10px;display:flex;gap:18px}
.topbar .links span{display:flex;align-items:center;gap:6px}

/* header */
.header{left:0;top:34px;width:1200px;height:79px;background:var(--white)}
.brand-name{font-family:"Raleway",sans-serif;font-weight:600;white-space:nowrap;letter-spacing:.5px}
.header .brand-name{left:128px;top:24px;font-size:28px;color:var(--brand)}
.contact-item{display:flex;gap:12px;align-items:center;font-size:10.5px;color:#555;line-height:15px}
.contact-phone{left:689px;top:20px}
.contact-hours{left:893px;top:20px}

/* nav */
.nav{left:0;top:113px;width:1200px;height:49px;background:var(--brand)}
.nav ul{list-style:none;display:flex;position:absolute;left:142px;top:17px;font-size:12px;color:var(--white)}
.nav li{padding:0 18px;border-left:1px solid rgba(255,255,255,.6);line-height:14px}
.nav li:first-child{border:none;padding-left:0;color:var(--cyan)}

/* hero */
.hero{left:0;top:162px;width:1200px;height:361px;background:linear-gradient(120deg,#3d4248 0%,#6b5c48 45%,#4a4f55 100%)}
.hero::after{content:"";position:absolute;inset:0;background:rgba(10,20,35,.35)}
.hero-copy{left:147px;top:98px;z-index:2;font-family:"Raleway",sans-serif;font-weight:300;font-size:42px;line-height:50px;color:#e7ebef}
.hero-copy b{font-family:"Poppins",sans-serif;font-weight:500;color:var(--cyan)}
.btn-solid{left:149px;top:266px;width:134px;height:36px;background:var(--brand);color:var(--white);font-size:11px;letter-spacing:.8px;display:flex;align-items:center;justify-content:center;z-index:2}
.slider-dots{left:166px;top:320px;z-index:2;display:flex;gap:6px;align-items:center}
.slider-dots .arrow{width:20px;height:20px;border-radius:50%;background:rgba(255,255,255,.35)}
.slider-dots .dot{width:7px;height:7px;border-radius:50%;background:#ddd}

.proposal{left:821px;top:0;width:213px;height:361px;background:rgba(30,40,50,.72);z-index:3}
.proposal .sup{position:absolute;left:0;width:100%;top:16px;text-align:center;color:var(--white);font-size:11px;letter-spacing:1px}
.proposal .title{position:absolute;left:0;width:100%;top:30px;text-align:center;color:var(--white);font-size:24px;letter-spacing:2px;font-family:"Raleway",sans-serif;font-weight:600}
.field{position:absolute;left:17px;width:179px;height:27px;background:var(--white);font-size:9px;color:var(--brand);padding:8px 8px}
.submit{position:absolute;left:17px;top:319px;width:179px;height:27px;background:var(--mid);color:var(--white);font-size:10px;letter-spacing:1px;text-align:center;line-height:27px}

/* about */
.about-kicker{left:127px;top:552px;font-family:"Raleway",sans-serif;font-weight:300;font-size:28px;color:var(--mid)}
.about-title{left:127px;top:584px;font-family:"Raleway",sans-serif;font-weight:700;font-size:30px;color:var(--navy);white-space:nowrap}
.timeline{left:138px;top:645px;width:8px;height:390px}
.about-text{left:166px;top:656px;width:250px;font-size:11.5px;line-height:19px;color:#555}
.about-text p+p{margin-top:18px}
.btn-outline{display:flex;align-items:center;justify-content:center;gap:8px;width:130px;height:36px;border:1.5px solid var(--brand);color:var(--brand);font-size:11px}
.btn-outline::after{content:"";position:absolute;left:-8px;top:8px;width:130px;height:36px;border-left:1.5px solid currentColor;border-bottom:1.5px solid currentColor;opacity:.7}
.about .btn-outline{left:171px;top:962px}
.ph1{left:474px;top:570px;width:273px;height:185px;background:linear-gradient(135deg,#4c5762,#b59a2e 55%,#5b6470)}
.ph2{left:757px;top:570px;width:273px;height:185px;background:linear-gradient(135deg,#c9c4bb,#8c6a4c 60%,#e2ded6)}
.ph3{left:474px;top:766px;width:273px;height:185px;background:linear-gradient(135deg,#2f3338,#7b7467 60%,#3a3d42)}
.ph4{left:757px;top:766px;width:273px;height:185px;background:linear-gradient(135deg,#4a4a46,#c9a53b 45%,#3b4048)}

/* process */
.process{left:0;top:1100px;width:1200px;height:166px;background:var(--mid);color:var(--white)}
.process h2{position:absolute;left:128px;top:24px;font-family:"Raleway",sans-serif;font-weight:300;font-size:28px}
.process h2 b{font-weight:700}
.process p{position:absolute;left:128px;top:70px;width:640px;font-size:11.5px;line-height:21px}
.process .btn-outline{position:absolute;left:853px;top:64px;color:var(--white);border-color:var(--white)}

/* benefits */
.benefits-photo{left:130px;top:1315px;width:446px;height:404px;background:linear-gradient(140deg,#6e5a44,#e6e3dc 45%,#d6d2c8 70%,#5a4734)}
.benefits-panel{left:576px;top:1315px;width:445px;height:404px;background:var(--deep);color:var(--white)}
.benefits-panel h2{position:absolute;left:115px;top:84px;font-family:"Raleway",sans-serif;font-weight:300;font-size:28px}
.benefits-panel h2 b{font-weight:700}
.benefits-panel p{position:absolute;left:115px;top:140px;width:236px;font-size:11.5px;line-height:19.5px}

/* empowered */
.empower{left:0;top:1774px;width:1200px;height:215px;background:linear-gradient(90deg,#3a3630,#5e5240 50%,#3a3630)}
.empower::after{content:"";position:absolute;inset:0;background:rgba(15,20,30,.45)}
.empower h2{position:absolute;z-index:2;width:100%;top:20px;text-align:center;color:var(--white);font-family:"Raleway",sans-serif;font-weight:300;font-size:28px}
.empower h2 b{font-weight:700}
.empower p{position:absolute;z-index:2;width:100%;top:64px;text-align:center;color:#e3e6ea;font-size:12px}
.empower .btn-outline{position:absolute;z-index:2;left:502px;top:124px;width:147px;height:40px;color:var(--white);border-color:var(--white)}

/* testimonials */
.clients-title{left:0;top:2030px;width:1200px;text-align:center;font-family:"Raleway",sans-serif;font-weight:300;font-size:30px;color:var(--mid)}
.clients-title b{font-weight:700;color:var(--navy)}
.clients-sub{left:0;top:2075px;width:1200px;text-align:center;font-size:11px;color:var(--grey)}
.quote{width:423px;height:143px;background:var(--soft);color:var(--white);font-size:10px;line-height:17.5px;padding:22px 24px 0 64px}
.quote .mark{position:absolute;left:18px;top:18px;width:36px;height:26px}
.quote::after{content:"";position:absolute;left:55px;bottom:-14px;border-left:14px solid transparent;border-right:14px solid transparent;border-top:14px solid var(--soft)}
.q1{left:145px;top:2138px}
.q2{left:587px;top:2138px}
.author{display:flex;align-items:center;gap:18px;font-size:10.5px;color:var(--grey)}
.author b{color:var(--navy);font-weight:600}
.avatar{width:56px;height:56px;border-radius:50%;background:linear-gradient(160deg,#e4d7cd,#a37c66)}
.a1{left:145px;top:2312px}
.a2{left:587px;top:2312px}

/* footer */
.footer{left:0;top:2417px;width:1200px;height:353px;background:linear-gradient(120deg,#2a323d,#4d5560 50%,#252c36)}
.footer::after{content:"";position:absolute;inset:0;background:rgba(18,24,32,.6)}
.footer .inner{position:absolute;inset:0;z-index:2;color:var(--white)}
.footer .brand-name{position:absolute;left:140px;top:80px;font-size:26px;color:var(--white)}
.f-about{position:absolute;left:140px;top:136px;width:380px;font-size:10.5px;line-height:19px;color:#e2e6ea}
.f-head{position:absolute;font-size:15px;font-weight:500;padding-left:10px;border-left:3px solid var(--cyan);line-height:18px}
.social{position:absolute;left:140px;top:270px;display:flex;gap:8px}
.social i{width:28px;height:28px;border-radius:50%;background:var(--white);display:block}
.f-links{position:absolute;left:570px;top:100px;width:170px;list-style:none;font-size:10.5px}
.f-links li{height:30px;border-bottom:1px dashed rgba(255,255,255,.35);display:flex;align-items:center;gap:10px}
.f-links li::before{content:"";width:8px;height:8px;border-radius:50%;border:1.5px solid var(--white)}
.f-contact{position:absolute;left:827px;top:98px;font-size:10.5px;line-height:17px;color:#e2e6ea}
.f-contact .row{position:absolute;left:0;display:flex;gap:16px;width:220px}
.f-contact svg{flex:none}
.bottombar{left:0;top:2770px;width:1200px;height:58px;background:var(--navy);color:#d5dde8;font-size:10px}
.bottombar .copy{position:absolute;left:134px;top:22px}
.bottombar .pay{position:absolute;left:722px;top:22px}
.cards{position:absolute;left:850px;top:18px;display:flex;gap:6px}
.cards i{display:block;width:32px;height:20px;border-radius:2px;background:#e6ebf2}
</style>
</head>
<body>

<div class="abs topbar">
  <div class="abs welcome">Welcome to the Halvorn Quantax</div>
  <div class="abs links">
    <span><svg width="9" height="9" viewBox="0 0 10 10"><circle cx="5" cy="3" r="2.5" fill="#c9d6e8"/><path d="M0 10a5 5 0 0 1 10 0z" fill="#c9d6e8"/></svg>Member Login</span>
    <span><svg width="9" height="9" viewBox="0 0 10 10"><rect x="1" y="4" width="8" height="6" fill="#c9d6e8"/><path d="M3 4V2.5a2 2 0 0 1 4 0V4" stroke="#c9d6e8" fill="none"/></svg>Signup</span>
    <span><svg width="10" height="8" viewBox="0 0 10 8"><rect width="10" height="8" fill="#c9d6e8"/><path d="M0 0l5 4 5-4" stroke="#0b2f5e" fill="none"/></svg>Contact</span>
  </div>
</div>

<header class="abs header">
  <div class="abs brand-name">Halvorn Quantax</div>
  <div class="abs contact-item contact-phone">
    <svg width="22" height="28" viewBox="0 0 22 28"><rect x="3" y="1" width="16" height="26" rx="2" fill="none" stroke="#0255a3" stroke-width="2"/><line x1="9" y1="23" x2="13" y2="23" stroke="#0255a3" stroke-width="2"/></svg>
    <div>(123) 555-0142<br>info@halvornquantax.com</div>
  </div>
  <div class="abs contact-item contact-hours">
    <svg width="26" height="26" viewBox="0 0 26 26"><circle cx="13" cy="13" r="11" fill="none" stroke="#0255a3" stroke-width="2"/><path d="M13 6v7l5 3" stroke="#0255a3" stroke-width="2" fill="none"/></svg>
    <div>9 am - 8 pm<br>Monday - Saturday</div>
  </div>
</header>

<nav class="abs nav">
  <ul><li>Home</li><li>Expertise</li><li>Takeoffs</li><li>Divisions Serviced</li><li>Member Login</li></ul>
</nav>

<section class="abs hero" role="img" aria-label="Dimmed photo of workers in hard hats on a commercial construction site">
  <div class="abs hero-copy"><b>Time</b> - in <b>Construction</b>, beyond<br>your <b>Reputation</b>, nothing is more<br><b>Valuable</b> than your time.</div>
  <div class="abs btn-solid">READ MORE</div>
  <div class="abs slider-dots"><span class="arrow"></span><span class="dot"></span><span class="dot"></span><span class="dot"></span><span class="arrow"></span></div>
  <form class="abs proposal">
    <div class="sup">REQUEST FOR</div>
    <div class="title">PROPOSAL</div>
    <div class="field" style="top:87px">Company Name</div>
    <div class="field" style="top:123px">Contact Name</div>
    <div class="field" style="top:159px">Phone</div>
    <div class="field" style="top:193px">Email</div>
    <div class="field" style="top:229px;height:83px">Message</div>
    <div class="submit">SUBMIT</div>
  </form>
</section>

<section class="about">
  <div class="abs about-kicker">About</div>
  <h2 class="abs about-title">Halvorn Quantax</h2>
  <svg class="abs timeline" viewBox="0 0 8 390"><circle cx="4" cy="4" r="4" fill="#0b2f5e"/><line x1="4" y1="4" x2="4" y2="386" stroke="#0b2f5e" stroke-width="2"/><circle cx="4" cy="386" r="4" fill="#0b2f5e"/></svg>
  <div class="abs about-text">
    <p>Dedicated to saving our clients time and money by specializing in accurate, reliable materials quantity calculations, Halvorn Quantax allows general contractors to confidently propose on more work with less stress.</p>
    <p>To receive a no-obligation answer to your takeoff needs complete the Request for Proposal form. Halvorn Quantax will provide a comprehensive proposal detailing the hours required and payment options that are easily refined to both near- and long-term needs.</p>
  </div>
  <div class="abs btn-outline">Read More <span>&#10140;</span></div>
  <div class="abs ph1" role="img" aria-label="Warehouse interior with yellow overhead crane"></div>
  <div class="abs ph2" role="img" aria-label="Bright open-plan office with white desks"></div>
  <div class="abs ph3" role="img" aria-label="Team working at laptops in a meeting"></div>
  <div class="abs ph4" role="img" aria-label="Group of workers in yellow hard hats"></div>
</section>

<section class="abs process">
  <h2>The <b>Process</b></h2>
  <p>Once the proposal is approved, clients fund their account and allocate their hours as desired - project-by-project, monthly, as-needed, or otherwise. Our service and products are completely tailored to each client based on the fundamental factors that make your business distinct from all others.</p>
  <div class="btn-outline">Read More <span>&#10140;</span></div>
</section>

<div class="abs benefits-photo" role="img" aria-label="Top view of hands sketching a flow chart beside a laptop and coffee"></div>
<section class="abs benefits-panel">
  <h2>The <b>Benefits</b></h2>
  <p>Accurate, reliable quantities delivered as-scheduled and expected allow your key staff to invest their time in quality, safety, profit, and client relationships. An extra set of hands in your bid room helps you put out more proposals and takes a tedious task off your to-do list whenever you need it without the obligation of a full-time salary.</p>
</section>

<section class="abs empower" role="img" aria-label="Dimmed photo of a crew in yellow hard hats">
  <h2>We <b>Empowered 1k Business</b></h2>
  <p>Registration is completely free...enrol now!</p>
  <div class="btn-outline">Register Now <span>&#10140;</span></div>
</section>

<h2 class="abs clients-title">What <b>Clients Say</b></h2>
<div class="abs clients-sub">The best of the best is here!</div>

<blockquote class="abs quote q1">
  <svg class="mark" viewBox="0 0 36 26"><path d="M0 0h15v14L8 26H2l5-12H0zM20 0h15v14l-7 12h-6l5-12h-7z" fill="#0b2f5e"/></svg>
  Halvorn Quantax does outstanding work, accurate, detailed, and reliable. The consultant on my account knows what I want in the breakdown and produces the information exactly as I need it. Time, money and confidence, Halvorn Quantax hits the mark every time.
</blockquote>
<blockquote class="abs quote q2">
  <svg class="mark" viewBox="0 0 36 26"><path d="M0 0h15v14L8 26H2l5-12H0zM20 0h15v14l-7 12h-6l5-12h-7z" fill="#0b2f5e"/></svg>
  We get an influx of great opportunities and sometimes it's more than we can handle. Halvorn Quantax fills the gap and helped us to grow our business. It's really excellent to have a genuine, always-ready ally in our estimating efforts.
</blockquote>
<div class="abs author a1"><span class="avatar" role="img" aria-label="Client portrait"></span><span><b>Dana Whitfield</b>, President Summit Ridge Roofing</span></div>
<div class="abs author a2"><span class="avatar" role="img" aria-label="Client portrait"></span><span><b>Owen Brandt</b>, Harborline Builders, LLC.</span></div>

<footer class="abs footer" role="img" aria-label="Dimmed photo of a team meeting around a table">
  <div class="inner">
    <div class="brand-name">Halvorn Quantax</div>
    <p class="f-about">Quantax theme is the essence of business themes. We recommend a winning generic strategy based on our insights &amp; experience in diverse businesses</p>
    <div class="f-head" style="left:140px;top:224px">Stay Connected</div>
    <div class="social"><i></i><i></i><i></i></div>
    <div class="f-head" style="left:570px;top:56px">Quick Links</div>
    <ul class="f-links"><li>Home</li><li>About us</li><li>Takeoffs</li><li>Services</li><li>Member Login</li><li>Contact</li></ul>
    <div class="f-head" style="left:827px;top:56px">Conact Us</div>
    <div class="f-contact">
      <div class="row" style="top:0"><svg width="18" height="16" viewBox="0 0 18 16"><path d="M9 0L0 8h3v8h4v-5h4v5h4V8h3z" fill="#fff"/></svg><span>Halvorn Quantax<br>PO Box 418, Fairhill,<br>GA 30120</span></div>
      <div class="row" style="top:66px"><svg width="18" height="22" viewBox="0 0 18 22"><rect x="3" y="1" width="12" height="20" rx="2" fill="none" stroke="#fff" stroke-width="2"/></svg><span>(555) 906-0127<br>(555) 925-0183</span></div>
      <div class="row" style="top:124px"><svg width="18" height="18" viewBox="0 0 18 18"><circle cx="9" cy="9" r="8" fill="#fff"/><path d="M9 4v5l3 2" stroke="#1d2530" stroke-width="2" fill="none"/></svg><span>Mon - Sat 9 am to 8 pm<br>Sun - 10 am to 3 pm</span></div>
      <div class="row" style="top:184px"><svg width="18" height="14" viewBox="0 0 18 14"><rect width="18" height="14" fill="#fff"/><path d="M0 0l9 7 9-7" stroke="#1d2530" fill="none"/></svg><span>info@halvornquantax.com</span></div>
    </div>
  </div>
</footer>

<div class="abs bottombar">
  <div class="copy">© 2019 Quantax. All rights reserved.</div>
  <div class="pay">We Proudly Accept</div>
  <div class="cards"><i></i><i></i><i></i><i></i></div>
</div>

</body>
</html>
```